依頼詳細
今回製作していただくのは泣き顔専用の「顔文字辞書アプリ」の画面の背景・ボタンデザインです。
オリジナルのボタンアイコンを制作と、それらを1枚のUIイメージ画像にまとめたものを提出して頂きます。

簡単なラフは下部に添付しております。

【必要な納品物】
・ラフを基に作成したUIイメージ画像(アイコンを配置したもの)1枚
・ブックマークアイコンON状態のもの 1点
・ブックマークアイコンOFF状態のもの 1点
・Newアイコン 1点
・お気に入りアイコン 1点
・ランダム表示アイコン 1点
・おすすめアプリアイコン 1点

※リテイクをお願いする可能性があります。
記載項目
UIイメージ画像:PNG 解像度:幅1536X高さ2048pxl
アイコン:PNG 512☓512px
希望イメージ
シンプル 複雑
単色 カラフル
暗い 明るい
日常 高級
遊び心 厳粛
未来的 伝統的
女性的 男性的
希望する色
納品ファイル
• 高解像度JPG (.jpg)
• イラストレーター形式 (.ai)
• PNG形式 (.png)
補足説明
■ 選んだ理由

クオリティが高く早めの納品や、修正依頼についても迅速に対応していただきました

■ 提案者全員のお礼・コメント

クオリティが高く早めの納品や、修正依頼についても迅速に対応していただきありがとうございます。
また機会がありましたら是非よろしくお願いします。

```html
<!DOCTYPE html>
<html lang="ja">
<head>
<meta charset="UTF-8">
<title>泣き顔 顔文字辞書</title>
<link rel="stylesheet" href="https://fonts.googleapis.com/css2?family=M+PLUS+Rounded+1c:wght@400;700&display=swap">
<style>
  :root{
    --bg:#fdf3ec;
    --card-top:#fffaf7;
    --card-bottom:#fbe6e6;
    --card-border:#f1cfd3;
    --cell:#f9d9dc;
    --cell-border:#efc0c6;
    --heart-on:#f39bb7;
    --heart-off:#fdeff1;
    --heart-off-line:#f6c9d3;
    --text:#4b3a3c;
    --scroll:#f3a6bf;
    --tab-top:#fff6f4;
    --tab-bottom:#fbe1e3;
    --tab-line:#f0c4cb;
    --pink:#f08cb3;
    --violet:#c99bd9;
  }
  *{margin:0;padding:0;box-sizing:border-box}
  html,body{width:900px;height:1200px;overflow:hidden;background:var(--bg)}
  .screen{position:relative;width:900px;height:1200px;overflow:hidden;background:var(--bg);
    font-family:"M PLUS Rounded 1c",sans-serif}
  .emoticon-list{list-style:none;position:absolute;left:0;top:-33px;width:900px}
  .emoticon-row{position:relative;height:117px;margin:0 45px 16px 15px;
    border:2px solid var(--card-border);border-radius:12px;overflow:hidden;
    background:linear-gradient(var(--card-top),var(--card-bottom));
    display:flex;align-items:center}
  .emoticon-text{flex:1;padding-left:34px;font-size:34px;color:var(--text);white-space:nowrap;letter-spacing:1px}
  .bookmark{width:122px;height:100%;background:var(--cell);border-left:2px solid var(--cell-border);
    display:flex;align-items:center;justify-content:center}
  .bookmark svg{width:72px;height:66px}
  .heart-on{fill:var(--heart-on)}
  .heart-off{fill:var(--heart-off);stroke:var(--heart-off-line);stroke-width:4}
  .scrollbar{position:absolute;right:14px;top:0;width:14px;height:300px;border-radius:7px;background:var(--scroll)}
  .tab-bar{position:absolute;left:0;bottom:0;width:900px;height:150px;
    background:linear-gradient(var(--tab-top),var(--tab-bottom));border-top:3px solid var(--tab-line);
    display:flex}
  .tab{flex:1;display:flex;flex-direction:column;align-items:center;justify-content:center;gap:4px}
  .tab svg{width:110px;height:84px}
  .tab-label{font-size:30px;font-weight:700;color:var(--pink)}
  .tab-label.violet{color:var(--violet)}
  .new-mark{font-family:"M PLUS Rounded 1c",sans-serif;font-size:58px;font-weight:700;fill:#fbd3e2}
</style>
</head>
<body>
<div class="screen">
  <svg width="0" height="0" style="position:absolute">
    <defs>
      <path id="heart" d="M50 88C20 65 6 48 6 30C6 16 17 6 30 6C40 6 46 12 50 20C54 12 60 6 70 6C83 6 94 16 94 30C94 48 80 65 50 88Z"/>
    </defs>
  </svg>

  <ul class="emoticon-list">
    <li class="emoticon-row"><span class="emoticon-text">号泣 No.01 ブワッ</span><span class="bookmark"><svg viewBox="0 0 100 94"><use href="#heart" class="heart-on"/></svg></span></li>
    <li class="emoticon-row"><span class="emoticon-text">大泣き No.02 ピー</span><span class="bookmark"><svg viewBox="0 0 100 94"><use href="#heart" class="heart-on"/></svg></span></li>
    <li class="emoticon-row"><span class="emoticon-text">涙目 No.03 ウッ…</span><span class="bookmark"><svg viewBox="0 0 100 94"><use href="#heart" class="heart-off"/></svg></span></li>
    <li class="emoticon-row"><span class="emoticon-text">絶叫 No.04 ウワァァン!!</span><span class="bookmark"><svg viewBox="0 0 100 94"><use href="#heart" class="heart-off"/></svg></span></li>
    <li class="emoticon-row"><span class="emoticon-text">感涙 No.05</span><span class="bookmark"><svg viewBox="0 0 100 94"><use href="#heart" class="heart-off"/></svg></span></li>
    <li class="emoticon-row"><span class="emoticon-text">泣き声 No.06 ウェーン</span><span class="bookmark"><svg viewBox="0 0 100 94"><use href="#heart" class="heart-on"/></svg></span></li>
    <li class="emoticon-row"><span class="emoticon-text">嘆き No.07 ウェェン</span><span class="bookmark"><svg viewBox="0 0 100 94"><use href="#heart" class="heart-off"/></svg></span></li>
    <li class="emoticon-row"><span class="emoticon-text">しくしく No.08</span><span class="bookmark"><svg viewBox="0 0 100 94"><use href="#heart" class="heart-on"/></svg></span></li>
  </ul>

  <div class="scrollbar"></div>

  <nav class="tab-bar">
    <div class="tab">
      <svg viewBox="0 0 110 84"><text class="new-mark" x="55" y="66" text-anchor="middle">New</text></svg>
      <span class="tab-label">新着</span>
    </div>
    <div class="tab">
      <svg viewBox="0 0 110 84">
        <g transform="translate(18 2) scale(0.78)"><use href="#heart" fill="#f7b6cf"/></g>
        <path d="M55 24v36M37 42h36" stroke="#fff" stroke-width="9" stroke-linecap="round"/>
      </svg>
      <span class="tab-label">お気に入り</span>
    </div>
    <div class="tab">
      <svg viewBox="0 0 110 84" fill="none" stroke="#d8b8e6" stroke-width="9" stroke-linecap="round" stroke-linejoin="round">
        <path d="M12 24h20c20 0 26 36 46 36h16"/>
        <path d="M12 60h20c20 0 26-36 46-36h16"/>
        <path d="M84 14l12 10-12 10M84 50l12 10-12 10"/>
      </svg>
      <span class="tab-label violet">ランダム</span>
    </div>
    <div class="tab">
      <svg viewBox="0 0 110 84" fill="none" stroke="#f5b3cb" stroke-width="6" stroke-linejoin="round" stroke-linecap="round">
        <path d="M22 10h66l8 66H14z" fill="#fde3ec"/>
        <path d="M40 26c0 20 30 20 30 0"/>
      </svg>
      <span class="tab-label">おすすめ</span>
    </div>
  </nav>
</div>
</body>
</html>
```